Vantry Forge (IT/Network Services)

Vantry Forge, LLC provides technology services to small and medium businesses. Essentially, anytime you've every thought your business might need an "IT guy" to handle something you could instead call us to handle it. Basically, you can outsource your IT needs to us.

This is a brand new company and so we'll need a brand new website. I'd like to use WordPress to handle the site since that will make things easier for me to maintain in the long run.

The site should include a, more-or-less, static front page with the dynamic data occurring on pages linked from a navigational area.

I have a logo already designed that I would like to see used in the design. The one with "white" in the title is the official logo, just added some other versions for your perusal.

Color queues from the logo but feel free to add other colors where applicable.

The site should feel somewhat corporate but with a "younger" slant (something a 25-35 year old would enjoy).

Pages (either to be added initially or by me after design completion):
"About" section - includes company history, business philosophy, etc.
"Services" section - service options, service approach, service specifics
"Testimonials" section - (eventually)
"News" section - (eventually) industry news, company news, events, blog
Contact Links

Websites to view:
The two largest local competitors:
http://www.harbelmsystemsinc.example/
http://www.qubrix.example/
Other local competitors:
http://www.plkllc.example/
http://www.merowaygroup.example/

Other info you might find useful:
Domain: vfllc.example
Address:
517 Calder Ln W
Suite 742B
Nashville, TN 37288
Phone: 615-555-0187
Emails available for use/display:
info@vfllc.example
sales@vfllc.example

Target Market(s)

Our target clients are mainly small businesses (25 or less computer users) which means we're looking at a lot of start-ups or younger companies. We'll be interacting with many entrepreneurs and young business owners.

Requirements
Must have
• Need full WP theme (not a mockup)

```html
<!DOCTYPE html>
<html lang="en">
<head>
<meta charset="utf-8">
<title>Vantry Forge — Technology Services</title>
<link href="https://fonts.googleapis.com/css2?family=Audiowide&family=Jura:wght@400;500;600&family=Open+Sans:ital,wght@0,400;0,600;0,700;1,700&display=swap" rel="stylesheet">
<style>
  :root {
    --orange: #f08a24;
    --orange-light: #f7a04a;
    --orange-dark: #e06f12;
    --ink: #3a3a3a;
    --grey-text: #555555;
    --grey-mid: #8a8a8a;
    --grey-light: #c9c9c9;
    --page: #f6f6f6;
    --footer-bg: #ececec;
    --panel: #e2e2e2;
    --white: #ffffff;
    --button-dark: #4a4a4a;
  }
  * { margin: 0; padding: 0; box-sizing: border-box; }
  html, body { width: 1182px; height: 1200px; overflow: hidden; }
  body {
    position: relative;
    background: var(--page);
    font-family: "Open Sans", Arial, sans-serif;
    color: var(--ink);
  }
  a { color: inherit; text-decoration: none; }
  .top-rule { position: absolute; left: 0; top: 0; width: 100%; height: 7px; background: linear-gradient(#3d3d3d, #6a6a6a); }
  .header-bg { position: absolute; left: 0; top: 7px; width: 100%; height: 510px;
    background: radial-gradient(ellipse at 50% 55%, #ffffff 0%, #f7f7f7 45%, #e6e6e6 100%); }

  .brand { position: absolute; left: 102px; top: 40px; display: flex; align-items: center; gap: 10px;
    font-family: "Audiowide", sans-serif; font-size: 32px; color: var(--orange); }
  .brand-dot { width: 14px; height: 14px; border-radius: 50%; background: var(--orange); }

  .main-nav { position: absolute; left: 433px; top: 53px; display: flex; font-family: "Jura", sans-serif; font-size: 16px; font-weight: 500; color: var(--grey-text); }
  .main-nav a { display: block; }
  .main-nav a:nth-child(1) { width: 150px; color: var(--orange); font-weight: 600; }
  .main-nav a:nth-child(2) { width: 146px; }
  .main-nav a:nth-child(3) { width: 140px; }
  .main-nav a:nth-child(4) { width: 86px; }

  .hero-art { position: absolute; left: 90px; top: 140px; width: 480px; height: 370px; border-radius: 50%;
    background: radial-gradient(ellipse at 45% 45%, #fbe7b0 0%, #eeeeee 35%, rgba(240,240,240,0) 70%); }
  .hero-title { position: absolute; left: 582px; top: 175px; width: 490px; white-space: nowrap; font-family: "Audiowide", sans-serif; font-weight: 400; font-size: 33px; color: var(--orange); }
  .hero-tagline { position: absolute; left: 582px; top: 226px; width: 500px; font-family: "Jura", sans-serif; font-weight: 500; font-size: 39px; line-height: 44px; color: var(--grey-text); }
  .hero-button { position: absolute; left: 582px; top: 400px; width: 248px; height: 44px; border-radius: 3px;
    background: linear-gradient(#6a6a6a, var(--button-dark)); box-shadow: 0 2px 3px rgba(0,0,0,.3);
    color: var(--white); font-family: "Audiowide", sans-serif; font-size: 18px; text-align: center; line-height: 44px; }
  .slider-dots { position: absolute; left: 986px; top: 470px; display: flex; gap: 8px; }
  .slider-dots span { width: 17px; height: 17px; border-radius: 50%; background: linear-gradient(#f5f5f5, #d6d6d6); }
  .slider-dots span.active { background: var(--orange); }
  .hero-divider { position: absolute; left: 60px; top: 516px; width: 1040px; height: 1px; background: linear-gradient(90deg, transparent, #d4d4d4 20%, #d4d4d4 80%, transparent); }

  .testimonial-icon { position: absolute; left: 105px; top: 565px; width: 52px; height: 52px; background: #f1efe6; box-shadow: 0 1px 3px rgba(0,0,0,.3); }
  .testimonial-title { position: absolute; left: 181px; top: 566px; font-family: "Jura", sans-serif; font-weight: 600; font-size: 21px; color: var(--grey-text); }
  .testimonial-quote { position: absolute; left: 181px; top: 609px; width: 390px; font-size: 14.2px; letter-spacing: -0.15px; line-height: 21px; color: var(--grey-text); }
  .testimonial-author { position: absolute; left: 182px; top: 728px; font-size: 11.5px; font-weight: 700; font-style: italic; line-height: 14px; color: var(--grey-text); }
  .read-more { position: absolute; left: 466px; top: 737px; font-family: "Audiowide", sans-serif; font-size: 13px; color: var(--orange); }

  .news-tabs { position: absolute; left: 582px; top: 562px; width: 480px; height: 196px; }
  .tab-bar { display: flex; height: 32px; }
  .tab { font-family: "Audiowide", sans-serif; font-size: 14px; line-height: 32px; text-align: center; color: var(--white);
    background: linear-gradient(var(--orange-light), var(--orange)); border-right: 1px solid var(--orange-dark); }
  .tab.active { background: var(--white); color: var(--orange); border: 1px solid #d0d0d0; border-bottom: none; width: 80px; }
  .tab.events { width: 107px; }
  .tab.blog { width: 99px; }
  .tab-panel { height: 164px; background: var(--white); border: 1px solid #d0d0d0; border-top: none; padding: 18px 12px 0 19px; }
  .news-item { position: relative; font-size: 13px; }
  .news-item::before { content: ""; position: absolute; left: -10px; top: 5px; width: 5px; height: 5px; border-radius: 50%; background: var(--orange); }
  .news-item time { display: block; font-size: 11px; color: var(--grey-mid); line-height: 14px; }
  .news-item p { font-weight: 700; line-height: 17px; color: var(--grey-text); }
  .news-item + .news-item { margin-top: 14px; padding-top: 18px; border-top: 1px solid #dedede; }
  .news-item + .news-item::before { top: 23px; }

  .newsletter { position: absolute; left: 102px; top: 813px; width: 960px; height: 100px; background: var(--white);
    border-radius: 8px 8px 0 0; box-shadow: 0 -1px 3px rgba(0,0,0,.12); }
  .newsletter h2 { position: absolute; left: 25px; top: 14px; font-family: "Audiowide", sans-serif; font-weight: 400; font-size: 22px; color: var(--orange); }
  .newsletter p { position: absolute; left: 25px; top: 42px; width: 475px; font-size: 14px; letter-spacing: -0.15px; line-height: 21px; color: var(--grey-text); }
  .newsletter-input { position: absolute; left: 509px; top: 45px; width: 298px; height: 32px; border-radius: 16px; border: 1px solid #dddddd; box-shadow: inset 0 2px 3px rgba(0,0,0,.08); background: var(--white); }
  .newsletter-submit { position: absolute; left: 819px; top: 45px; width: 119px; height: 32px; border-radius: 16px;
    background: linear-gradient(var(--orange-light), var(--orange-dark)); box-shadow: 0 2px 3px rgba(0,0,0,.25);
    color: var(--white); font-family: "Audiowide", sans-serif; font-size: 15px; text-align: center; line-height: 32px; }
  .footer-band { position: absolute; left: 0; top: 912px; width: 100%; height: 14px; background: linear-gradient(#bdbdbd, #f4f4f4 35%, #e6e6e6); }

  .site-footer { position: absolute; left: 0; top: 926px; width: 100%; height: 274px; background: var(--footer-bg); }
  .footer-address { position: absolute; left: 102px; top: 42px; font-size: 12.5px; line-height: 17px; color: var(--ink); font-style: normal; }
  .footer-address strong { font-weight: 700; }
  .copyright { position: absolute; left: 102px; top: 178px; font-size: 12.5px; line-height: 17px; color: var(--grey-text); }
  .footer-links { position: absolute; left: 338px; top: 43px; width: 478px; height: 174px; border-radius: 14px;
    background: var(--panel); border-bottom: 6px solid var(--white); box-shadow: inset 0 3px 4px rgba(0,0,0,.08); }
  .footer-col { position: absolute; top: 29px; font-size: 11.5px; line-height: 14.6px; color: var(--grey-text); }
  .footer-col h3 { font-size: 12.5px; font-weight: 700; color: var(--grey-text); margin-bottom: 15px; }
  .footer-col a { display: block; }
  .col-home { left: 21px; }
  .col-about { left: 110px; }
  .col-tech { left: 221px; }
  .col-follow { left: 375px; }
  .col-follow h3 { margin-bottom: 12px; }
  .col-follow a { display: flex; align-items: center; gap: 8px; line-height: 19px; }
  .social-square { width: 16px; height: 16px; border-radius: 2px; background: #3d5a98; }
  .social-square.s2 { background: #3aa8e0; }
  .social-square.s3 { background: #1f74ad; }
  .social-square.s4 { background: #b92020; }
  .social-square.s5 { background: var(--orange); }
  .footer-mark { position: absolute; left: 852px; top: 92px; font-family: "Audiowide", sans-serif; font-size: 26px; color: var(--grey-light); }
</style>
</head>
<body>
  <div class="top-rule"></div>
  <div class="header-bg"></div>

  <header>
    <a class="brand" href="#"><span>Vantry Forge</span><span class="brand-dot"></span></a>
    <nav class="main-nav">
      <a href="#">Who We Are?</a>
      <a href="#">Our Services</a>
      <a href="#">Testimonials</a>
      <a href="#">News</a>
      <a href="#">Contact Us</a>
    </nav>
  </header>

  <section class="hero">
    <div class="hero-art" role="img" aria-label="Illustration of servers linked by network cables to a central yellow folder"></div>
    <h1 class="hero-title">Hello, we're Vantry Forge.</h1>
    <p class="hero-tagline">We provide technology services to small and medium businesses</p>
    <a class="hero-button" href="#">view our services</a>
    <div class="slider-dots"><span class="active"></span><span></span><span></span></div>
  </section>
  <div class="hero-divider"></div>

  <section class="testimonial">
    <div class="testimonial-icon" role="img" aria-label="Notepad with a pencil"></div>
    <h2 class="testimonial-title">What our Clients are saying!</h2>
    <p class="testimonial-quote">Lorem ipsum dolor sit amet, consectetuer adipiscing elit, sed diam nonummy nibh euismod tincidunt ut laoreet dolore magna aliquam erat volutpat. Ut wisi enim ad min im veniam, quis nostrud exerci tation ullamcorper susci pit lobortis nisl ut aliquip ex ea commodo.</p>
    <p class="testimonial-author">—Dalen R. Whitcombe, P.E.<br>Corveld Engineering, Inc.</p>
    <a class="read-more" href="#">read more &gt;</a>
  </section>

  <section class="news-tabs">
    <div class="tab-bar">
      <span class="tab active">News</span>
      <span class="tab events">Events</span>
      <span class="tab blog">Blog</span>
    </div>
    <div class="tab-panel">
      <article class="news-item">
        <time>May 31, 2012</time>
        <p>Lorem ipsum dolor sit amet, consectetuer adipiscing elit, sed diam nonummy nibh euismod tincidunt ut laoreet dolore.</p>
      </article>
      <article class="news-item">
        <time>April 30, 2012</time>
        <p>Lorem ipsum dolor sit amet, consectetuer adipiscing elit, sed diam nonummy nibh euismod tincidunt ut laoreet dolore.</p>
      </article>
    </div>
  </section>

  <section class="newsletter">
    <h2>Email Newsletter</h2>
    <p>Enter your email address to receive monthly updates about our latest news, events and free technology resources for your small business!</p>
    <div class="newsletter-input"></div>
    <a class="newsletter-submit" href="#">submit</a>
  </section>
  <div class="footer-band"></div>

  <footer class="site-footer">
    <address class="footer-address">
      <strong>Vantry Forge LLC.</strong><br>
      517 Calder Ln W<br>
      Suite 742B<br>
      Nashville, TN 37288
    </address>
    <p class="copyright">© Copyright 2012 Vantry Forge LLC.<br>All Rights Reserved.</p>

    <nav class="footer-links">
      <div class="footer-col col-home">
        <h3>Home</h3>
        <a href="#">Contact Us</a>
        <a href="#">Sitemap</a>
      </div>
      <div class="footer-col col-about">
        <h3>About Us</h3>
        <a href="#">Overview</a>
        <a href="#">Executive Team</a>
        <a href="#">News</a>
        <a href="#">Events</a>
        <a href="#">Blog</a>
      </div>
      <div class="footer-col col-tech">
        <h3>Technology</h3>
        <a href="#">Overview</a>
        <a href="#">Onsite Expertise</a>
        <a href="#">IT Design Services</a>
        <a href="#">Virus &amp; Spam Protection</a>
        <a href="#">Archiving</a>
      </div>
      <div class="footer-col col-follow">
        <h3>Follow Us</h3>
        <a href="#"><span class="social-square"></span>Friendloop</a>
        <a href="#"><span class="social-square s2"></span>Chirpline</a>
        <a href="#"><span class="social-square s3"></span>Workgraph</a>
        <a href="#"><span class="social-square s4"></span>Viewcast</a>
        <a href="#"><span class="social-square s5"></span>Rss Feed</a>
      </div>
    </nav>

    <div class="footer-mark">Vantry Forge</div>
  </footer>
</body>
</html>
```